Business Card Design

We need a business card designed for our new company. Prefer a black card with white logo & writing.

Contact Information for Business Card

Dov Telling, address: 3-4817 Fernwick Avenue, Abbotsford, BC, V8K 2P9, Office Phone: 604-913-2760, Cell: 604-271-4053, Email: dov@qlresinhaus.ca

Colors

Designer to choose only greyscale colors for use in the design.

```html
<!DOCTYPE html>
<html lang="en">
<head>
<meta charset="utf-8">
<title>QL Resin Haus – Business Card</title>
<link href="https://fonts.googleapis.com/css2?family=Montserrat:wght@400;500;600;700&display=swap" rel="stylesheet">
<style>
  :root {
    --page: #2a2a2a;
    --card: #151515;
    --ink: #ffffff;
    --ink-soft: #e6e6e6;
    --band: #ffffff;
    --band-ink: #555555;
    --mark: #3a3a3a;
  }
  * { margin: 0; padding: 0; box-sizing: border-box; }
  html, body { width: 1200px; height: 1059px; overflow: hidden; }
  body {
    background: var(--page);
    font-family: "Montserrat", sans-serif;
    position: relative;
  }
  .card {
    position: absolute;
    background: var(--card);
    border-radius: 20px;
    overflow: hidden;
    box-shadow: 0 8px 20px rgba(0,0,0,.55);
  }
  .card-front { left: 256px; top: 89px; width: 688px; height: 390px; }
  .card-back  { left: 252px; top: 546px; width: 696px; height: 394px; }
  .brand-name {
    position: absolute;
    left: 0; right: 0;
    text-align: center;
    color: var(--ink);
    font-weight: 700;
    letter-spacing: 1px;
    line-height: 1;
  }
  .card-front .brand-name { top: 170px; font-size: 52px; }
  .card-back .brand-name  { top: 104px; font-size: 34px; }
  .person {
    position: absolute;
    right: 369px;
    top: 247px;
    text-align: right;
    color: var(--ink);
  }
  .person-name { font-size: 28px; font-weight: 600; line-height: 1.2; }
  .person-title { font-size: 17px; font-weight: 400; color: var(--ink-soft); margin-top: 4px; }
  .divider {
    position: absolute;
    left: 353px; top: 245px;
    width: 2px; height: 72px;
    background: var(--ink);
  }
  .contacts {
    position: absolute;
    left: 377px; top: 240px;
    list-style: none;
    color: var(--ink);
    font-size: 18px;
    line-height: 27.5px;
  }
  .contacts li { display: flex; align-items: center; gap: 8px; }
  .contacts svg { width: 15px; height: 15px; fill: var(--ink); flex: none; }
  .address-band {
    position: absolute;
    left: 0; right: 0; top: 347px;
    height: 25px;
    background: var(--band);
    color: var(--band-ink);
    font-size: 17px;
    line-height: 25px;
  }
  .address-band .address { position: absolute; left: 118px; }
  .address-band .dot {
    position: absolute;
    left: 624px; top: -1px;
    width: 27px; height: 27px;
    border-radius: 50%;
    background: var(--mark);
  }
</style>
</head>
<body>
  <section class="card card-front">
    <div class="brand-name">QL RESIN HAUS</div>
  </section>

  <section class="card card-back">
    <div class="brand-name">QL RESIN HAUS</div>

    <div class="person">
      <div class="person-name">Dov Telling</div>
      <div class="person-title">Owner/CEO</div>
    </div>
    <div class="divider"></div>

    <ul class="contacts">
      <li>
        <svg viewBox="0 0 16 16" aria-hidden="true"><path d="M2 6c0-2 2.5-3.5 6-3.5S14 4 14 6l-3 .8V5.5H5v1.3zM4 8h8l1.5 5h-11z"/></svg>
        604-913-2760
      </li>
      <li>
        <svg viewBox="0 0 16 16" aria-hidden="true"><path d="M5 1h6a1 1 0 0 1 1 1v12a1 1 0 0 1-1 1H5a1 1 0 0 1-1-1V2a1 1 0 0 1 1-1zm.3 1.5v10h5.4v-10zM8 13.2a.6.6 0 1 0 0 1.2.6.6 0 0 0 0-1.2z"/></svg>
        604-271-4053
      </li>
      <li>
        <svg viewBox="0 0 16 16" aria-hidden="true"><path d="M1 5l7-4 7 4v9H1zm1.5 1.2v6.3l3.8-3.1zm11 0L9.7 9.4l3.8 3.1zM3 13.5h10L8.8 10 8 10.6 7.2 10z"/></svg>
        dov@qlresinhaus.ca
      </li>
    </ul>

    <div class="address-band">
      <span class="address">3-4817 Fernwick Avenue, Abbotsford, BC, V8K 2P9</span>
      <span class="dot"></span>
    </div>
  </section>
</body>
</html>
```